Resume for higher management position in a mechanical/consultant industries application*

I would like to use this resume for getting a higher position interview possibilities. My skills are multi-cultural negotiation, mechanical industry sales, outsourcing to Asia, ability to manage the agent/reseller system, well team player. multi-language Chinese/English/German specialized. Please make the design, professional, comfortable to read atmosphere.

Target Market(s)

management position, sales related

Font styles to use
Serif
Sans Serif

```html
<!DOCTYPE html>
<html lang="en">
<head>
<meta charset="utf-8">
<title>Yun-Ting Kuo — Resume</title>
<link href="https://fonts.googleapis.com/css2?family=Noto+Serif:wght@400;700&display=swap" rel="stylesheet">
<style>
  :root{
    --ink:#161b22;
    --paper:#ffffff;
    --snow:#eef2f0;
    --sidebar-w:337px;
  }
  *{margin:0;padding:0;box-sizing:border-box;}
  html,body{width:848px;height:1200px;overflow:hidden;background:var(--paper);}
  body{font-family:"Noto Serif",Georgia,serif;color:var(--ink);}
  .resume{position:relative;width:848px;height:1200px;overflow:hidden;}
  .sidebar{position:absolute;left:0;top:0;width:var(--sidebar-w);height:1200px;background:var(--ink);color:var(--paper);}
  .abs{position:absolute;line-height:1;white-space:nowrap;}

  .name-initial{left:273px;top:44px;font-size:112px;color:var(--snow);z-index:2;}
  .name-rest{left:334px;top:75px;font-size:76px;color:var(--ink);letter-spacing:0.5px;}
  .name-rule{position:absolute;left:5px;top:157px;width:328px;height:1.5px;background:var(--paper);}

  .side-heading{position:absolute;right:25px;font-size:20px;font-weight:700;color:var(--paper);line-height:1;}
  .side-rule{position:absolute;left:82px;width:228px;height:1.5px;background:var(--paper);}

  .profile-text{position:absolute;left:40px;top:231px;width:266px;font-size:17px;line-height:20.8px;text-align:justify;text-align-last:right;color:var(--paper);}

  .contact{position:absolute;right:56px;font-size:19.5px;line-height:1;text-align:right;color:var(--paper);}
  .contact-icon{position:absolute;left:289px;width:25px;height:25px;}
  .address{line-height:22.5px;}

  .edu{position:absolute;right:54px;font-size:16px;line-height:19px;text-align:right;color:var(--paper);}
  .edu-icon{position:absolute;left:289px;width:30px;height:20px;}

  .main-heading{position:absolute;left:362px;font-size:37px;font-weight:400;line-height:1;color:var(--ink);}
  .main-rule{position:absolute;left:362px;width:418px;height:1.5px;background:var(--ink);}

  .job{position:absolute;width:420px;}
  .job-icon{position:absolute;left:0;top:2px;width:26px;height:22px;}
  .job-body{margin-left:34px;}
  .job-title,.job-company{font-size:20.5px;font-weight:700;line-height:24.5px;}
  .job-desc{font-size:17px;line-height:20.8px;white-space:nowrap;}

  .skills-text{position:absolute;left:385px;top:953px;font-size:17px;line-height:20.8px;white-space:nowrap;}
</style>
</head>
<body>
<div class="resume">
  <aside class="sidebar">
    <div class="name-rule"></div>

    <h2 class="side-heading" style="top:190px;">Profile:</h2>
    <div class="side-rule" style="top:212px;"></div>
    <p class="profile-text">Short summary about you highlighting only the very important points in short. Try not to fill this area with too much information. Positioning may require small modifications.</p>

    <h2 class="side-heading" style="top:450px;">Personal Information:</h2>
    <div class="side-rule" style="top:472px;"></div>

    <div class="contact" style="top:491px;">9876543210</div>
    <svg class="contact-icon" style="top:484px;" viewBox="0 0 24 24" aria-hidden="true"><path fill="#fff" d="M6.6 2.2l2.6 4.1c.3.5.2 1.1-.2 1.5L7.4 9.3c1.2 2.7 3.9 5.4 6.6 6.6l1.5-1.6c.4-.4 1-.5 1.5-.2l4.1 2.6c.5.3.7 1 .4 1.5l-1.3 2.4c-.4.7-1.2 1.1-2 .9C10.1 19.8 4.2 13.9 2.5 6c-.2-.8.2-1.6.9-2l2.4-1.3c.3-.2.6-.3.8-.5z"/><path fill="none" stroke="#fff" stroke-width="1.6" stroke-linecap="round" d="M14 3.5a7 7 0 0 1 6.5 6.5M14 7a3.6 3.6 0 0 1 3 3"/></svg>

    <div class="contact" style="top:518px;">username@domain.com</div>
    <svg class="contact-icon" style="top:515px;" viewBox="0 0 24 24" aria-hidden="true"><rect x="1" y="4" width="22" height="16" fill="none" stroke="#fff" stroke-width="1.8"/><path d="M1 4l11 9 11-9M1 20l8.5-8M23 20l-8.5-8" fill="none" stroke="#fff" stroke-width="1.6"/></svg>

    <div class="contact" style="top:550px;right:53px;">professional profile address</div>
    <svg class="contact-icon" style="top:546px;" viewBox="0 0 24 24" aria-hidden="true"><rect x="0.5" y="0.5" width="23" height="23" rx="2" fill="#fff"/></svg>

    <div class="contact" style="top:587px;">MM/DD/YYYY</div>
    <svg class="contact-icon" style="top:582px;" viewBox="0 0 24 24" aria-hidden="true"><rect x="1" y="3" width="22" height="20" fill="#e6e8ea"/><rect x="1" y="3" width="22" height="5" fill="#fff"/><rect x="5" y="0.5" width="2.5" height="5" fill="#fff"/><rect x="16.5" y="0.5" width="2.5" height="5" fill="#fff"/><path d="M8 17h8M12 11v6M9 19h6" stroke="var(--ink)" stroke-width="1.4"/></svg>

    <div class="contact address" style="top:619px;right:56px;">Address Line 1<br>Address Line 2<br>Address Line 3</div>
    <svg class="contact-icon" style="top:619px;height:30px;" viewBox="0 0 24 30" aria-hidden="true"><path fill="#fff" d="M12 0C6 0 2 4.4 2 10c0 7 10 20 10 20s10-13 10-20C22 4.4 18 0 12 0zm0 14a4 4 0 1 1 0-8 4 4 0 0 1 0 8z"/></svg>

    <h2 class="side-heading" style="top:762px;">Education:</h2>
    <div class="side-rule" style="top:784px;"></div>

    <div class="edu" style="top:801px;">MBA<br>Lombardia Institute of Technology, Italy<br>2011-2012</div>
    <svg class="edu-icon" style="top:799px;" viewBox="0 0 30 20" aria-hidden="true"><path fill="#fff" d="M15 1L1 7l14 6 14-6z"/><path fill="#fff" d="M7 10v5c2 2.5 14 2.5 16 0v-5l-8 3.5z"/><path d="M3 8v7" stroke="#fff" stroke-width="1.4"/></svg>

    <div class="edu" style="top:874px;">Bachelor of Chemical Engineering<br>Tao-Shan Polytechnic University<br>2005-2009</div>
    <svg class="edu-icon" style="top:872px;" viewBox="0 0 30 20" aria-hidden="true"><path fill="#fff" d="M15 1L1 7l14 6 14-6z"/><path fill="#fff" d="M7 10v5c2 2.5 14 2.5 16 0v-5l-8 3.5z"/><path d="M3 8v7" stroke="#fff" stroke-width="1.4"/></svg>
  </aside>

  <h1>
    <span class="abs name-initial">Y</span><span class="abs name-rest">un-Ting Kuo</span>
  </h1>

  <main>
    <h2 class="main-heading" style="top:208px;">Experience:</h2>
    <div class="main-rule" style="top:247px;"></div>

    <article class="job" style="left:362px;top:257px;">
      <svg class="job-icon" viewBox="0 0 26 22" aria-hidden="true"><path fill="var(--ink)" d="M9 0h8a2 2 0 0 1 2 2v2h5a2 2 0 0 1 2 2v5H16v-1h-6v1H0V6a2 2 0 0 1 2-2h5V2a2 2 0 0 1 2-2zm1 2v2h6V2zM0 12h10v2h6v-2h10v8a2 2 0 0 1-2 2H2a2 2 0 0 1-2-2z"/></svg>
      <div class="job-body">
        <div class="job-title">Designation | Year - Current</div>
        <div class="job-company">Company Name, Country</div>
        <p class="job-desc">One or two line about your contribution to this<br>company, how you were an asset to them. Any<br>special skills you posses or any relevant or signif-<br>icant problem you solved and how.</p>
      </div>
    </article>

    <article class="job" style="left:359px;top:406px;">
      <svg class="job-icon" viewBox="0 0 26 22" aria-hidden="true"><path fill="var(--ink)" d="M9 0h8a2 2 0 0 1 2 2v2h5a2 2 0 0 1 2 2v5H16v-1h-6v1H0V6a2 2 0 0 1 2-2h5V2a2 2 0 0 1 2-2zm1 2v2h6V2zM0 12h10v2h6v-2h10v8a2 2 0 0 1-2 2H2a2 2 0 0 1-2-2z"/></svg>
      <div class="job-body">
        <div class="job-title">Designation | Year - Current</div>
        <div class="job-company">Company Name, Country</div>
        <p class="job-desc">One or two line about your contribution to this<br>company, how you were an asset to them. Any<br>special skills you posses or any relevant or signif-<br>icant problem you solved and how.</p>
      </div>
    </article>

    <article class="job" style="left:354px;top:555px;">
      <svg class="job-icon" viewBox="0 0 26 22" aria-hidden="true"><path fill="var(--ink)" d="M9 0h8a2 2 0 0 1 2 2v2h5a2 2 0 0 1 2 2v5H16v-1h-6v1H0V6a2 2 0 0 1 2-2h5V2a2 2 0 0 1 2-2zm1 2v2h6V2zM0 12h10v2h6v-2h10v8a2 2 0 0 1-2 2H2a2 2 0 0 1-2-2z"/></svg>
      <div class="job-body">
        <div class="job-title">Designation | Year - Current</div>
        <div class="job-company">Company Name, Country</div>
        <p class="job-desc">One or two line about your contribution to this<br>company, how you were an asset to them. Any<br>special skills you posses or any relevant or signif-<br>icant problem you solved and how.</p>
      </div>
    </article>

    <article class="job" style="left:351px;top:710px;">
      <svg class="job-icon" viewBox="0 0 26 22" aria-hidden="true"><path fill="var(--ink)" d="M9 0h8a2 2 0 0 1 2 2v2h5a2 2 0 0 1 2 2v5H16v-1h-6v1H0V6a2 2 0 0 1 2-2h5V2a2 2 0 0 1 2-2zm1 2v2h6V2zM0 12h10v2h6v-2h10v8a2 2 0 0 1-2 2H2a2 2 0 0 1-2-2z"/></svg>
      <div class="job-body">
        <div class="job-title">Designation | Year - Current</div>
        <div class="job-company">Company Name, Country</div>
        <p class="job-desc">One or two line about your contribution to this<br>company, how you were an asset to them. Any<br>special skills you posses or any relevant or signif-<br>icant problem you solved and how.</p>
      </div>
    </article>

    <h2 class="main-heading" style="top:894px;">Special Skills:</h2>
    <div class="main-rule" style="top:935px;"></div>
    <p class="skills-text">Anyother relevant point you might want to add<br>about yourself or your experience. Try to write<br>these in bullet points.</p>
  </main>
</div>
</body>
</html>
```